clean web design for a recruitment company

We need a web design for a company called 'TORAVI' recruitment. We are a new age recruitment companies that selects people by their true nature, values and what they can bring to the table as a tangible talent. We are all here possessing a certain talent, whatever that could be that the world needs. The final design should communicate professionalism and strongly embedded etiquette we believe in and a branding promise 'Seeing ones true nature'. Our companies values are integrity, giving away to the community, cherishing the sharing of our talent, time and helping one another.

Target Market(s)

Gulf Countries

Industry/Entity Type

It Company

Number of Pages Required

1 page

Font styles to use
Serif

Requirements
Must have
• Clear and readable font, user friendly structure and easy navigation menus.
Nice to have
• Extra sort of ideas on images we may use, tag lines etc. sample sites we love site:https://www.velmaroque.com/
• http://www.dorisaklund.com/
• http://www.pebblemoorhouse.com/idea-gallery/
Should not have
• all sort of colors, big combination of fonts, images with people in the office or people in suits likewise all the typical industry web sites

```html
<!DOCTYPE html>
<html lang="en">
<head>
<meta charset="utf-8">
<title>Toravi Recruitment</title>
<link rel="stylesheet" href="https://fonts.googleapis.com/css2?family=Roboto+Condensed:wght@700&family=Lato:wght@300&family=Noto+Serif:wght@400;700&family=Tinos&display=swap">
<style>
  :root {
    --white: #ffffff;
    --ink: #111111;
    --nav-active: #0d0d0d;
    --hero-dark: #3a3a3a;
    --hero-light: #8c8c8c;
    --band: rgba(40, 40, 40, 0.55);
    --panel: #121212;
    --panel-highlight: #4a4a4a;
    --rule: #6a6a6a;
  }
  * { margin: 0; padding: 0; box-sizing: border-box; }
  html, body { width: 1200px; height: 900px; overflow: hidden; background: var(--panel); }
  .page { position: relative; width: 1200px; height: 900px; }

  .site-header { position: absolute; left: 0; top: 0; width: 1200px; height: 94px; background: var(--white); }
  .brand { position: absolute; left: 128px; top: 18px; display: flex; align-items: center; gap: 8px;
    font-family: "Roboto Condensed", sans-serif; font-weight: 700; font-size: 22px; color: var(--ink); letter-spacing: 1px; }
  .brand-mark { width: 14px; height: 14px; background: var(--ink); }
  .brand-sub { position: absolute; left: 150px; top: 68px; font-family: "Roboto Condensed", sans-serif; font-weight: 700;
    font-size: 8px; letter-spacing: 1.5px; color: var(--ink); }

  .main-nav a { position: absolute; top: 0; height: 94px; line-height: 110px; transform: translateX(-50%);
    font-family: "Roboto Condensed", sans-serif; font-weight: 700; font-size: 20px; color: var(--ink);
    text-decoration: none; white-space: nowrap; }
  .main-nav a.is-active { left: 393px; width: 74px; background: var(--nav-active); color: var(--white); text-align: center; }

  .hero { position: absolute; left: 0; top: 94px; width: 1200px; height: 483px;
    background: linear-gradient(180deg, #2e2e2e 0%, var(--hero-light) 30%, #6f6f6f 60%, #4a4440 80%, var(--hero-dark) 100%); }
  .hero-band { position: absolute; left: 0; top: 183px; width: 1200px; height: 56px; background: var(--band); }
  .hero-tagline { position: absolute; left: 0; top: 180px; width: 1200px; text-align: center;
    font-family: "Lato", sans-serif; font-weight: 300; font-size: 48px; color: var(--white); }

  .services { position: absolute; left: 0; top: 577px; width: 1200px; height: 323px; background: var(--panel); }
  .services-highlight { position: absolute; left: 34px; top: 0; width: 272px; height: 323px; background: var(--panel-highlight); }

  .service-icon { position: absolute; top: 44px; }
  .service-title { position: absolute; top: 50px; font-family: "Noto Serif", serif; font-size: 19px; color: var(--white); white-space: nowrap; }
  .service-title strong { font-weight: 700; }
  .service-rule { position: absolute; top: 102px; height: 1px; background: var(--rule); }
  .service-text { position: absolute; top: 115px; width: 250px; font-family: "Tinos", serif; font-size: 14px;
    line-height: 17px; color: var(--white); }
  .service-button { position: absolute; top: 234px; height: 28px; border: 1px solid var(--white);
    font-family: "Tinos", serif; font-size: 14px; color: var(--white); line-height: 26px; text-align: center; }
</style>
</head>
<body>
<div class="page">
  <header class="site-header">
    <div class="brand"><span class="brand-mark"></span>toravi</div>
    <div class="brand-sub">RECRUITMENT</div>
    <nav class="main-nav">
      <a class="is-active" href="#">Home</a>
      <a href="#" style="left:477px">Team</a>
      <a href="#" style="left:582px">Methodology</a>
      <a href="#" style="left:722px">Specialist Atreas</a>
      <a href="#" style="left:839px">Clinets</a>
      <a href="#" style="left:939px">Candidates</a>
      <a href="#" style="left:1064px">Toravi Group</a>
    </nav>
  </header>

  <section class="hero" role="img" aria-label="Gallery wall of black and white portrait photographs with a visitor walking past">
    <div class="hero-band"></div>
    <h1 class="hero-tagline">Seeing ones true nature</h1>
  </section>

  <section class="services">
    <div class="services-highlight"></div>

    <svg class="service-icon" style="left:99px" width="30" height="38" viewBox="0 0 30 38" aria-hidden="true">
      <path d="M2 2h18l8 8v26H2z" fill="none" stroke="#fff" stroke-width="2"/>
      <path d="M20 2v8h8" fill="none" stroke="#fff" stroke-width="2"/>
      <path d="M8 17h14M8 22h14M8 27h14M8 32h14" stroke="#fff" stroke-width="2"/>
    </svg>
    <h2 class="service-title" style="left:144px"><strong>Find</strong> a Job</h2>
    <div class="service-rule" style="left:48px;width:237px"></div>
    <p class="service-text" style="left:53px">Lorem ipsum dolor sit amet, consectetur adipiscing elit, sed do eiusmod tempor incididunt ut labore et dolore magna aliqua. Ut enim ad minim veniam, quis nostrud exercitation ullamco laboris nisi</p>
    <a class="service-button" style="left:53px;width:88px">Search Jobs</a>

    <svg class="service-icon" style="left:443px" width="30" height="38" viewBox="0 0 30 38" aria-hidden="true">
      <path d="M2 2h18l8 8v26H2z" fill="none" stroke="#fff" stroke-width="2"/>
      <path d="M20 2v8h8" fill="none" stroke="#fff" stroke-width="2"/>
      <path d="M8 17h14M8 22h14M8 27h14M8 32h14" stroke="#fff" stroke-width="2"/>
    </svg>
    <h2 class="service-title" style="left:489px"><strong>Find</strong> employes</h2>
    <div class="service-rule" style="left:393px;width:237px"></div>
    <p class="service-text" style="left:398px">Lorem ipsum dolor sit amet, consectetur adipiscing elit, sed do eiusmod tempor incididunt ut labore et dolore magna aliqua. Ut enim ad minim veniam, quis nostrud exercitation ullamco laboris nisi</p>
    <a class="service-button" style="left:397px;width:87px">Search Talent</a>

    <svg class="service-icon" style="left:818px;top:40px" width="47" height="46" viewBox="0 0 47 46" aria-hidden="true">
      <circle cx="23.5" cy="12" r="11" fill="#fff"/>
      <path d="M1 46c0-14 10-21 22.5-21S46 32 46 46z" fill="#fff"/>
    </svg>
    <h2 class="service-title" style="left:875px"><strong>Talent</strong> Portal</h2>
    <div class="service-rule" style="left:779px;width:238px"></div>
    <p class="service-text" style="left:785px">Lorem ipsum dolor sit amet, consectetur adipiscing elit, sed do eiusmod tempor incididunt ut labore et dolore magna aliqua. Ut enim ad minim veniam, quis nostrud exercitation ullamco laboris nisi</p>
    <a class="service-button" style="left:784px;width:87px">Register</a>
    <a class="service-button" style="left:930px;width:87px">Login</a>
  </section>
</div>
</body>
</html>
```